Alaska Real Estate Business Card

I need a new business card that uses my new logo, has my headshot and is not something cookie cutter from the typical business card websites. I want it to some what match my existing business card but matches more to my new logo. I am not a flashy person so I would like my business card to be unique but at the same time conservative.

Target Market(s)

People that will be purchasing real estate.

Industry/Entity Type

Real Estate Agent

Contact Information for Business Card

Business Card that has a style that blends with my logo and only has 2-3 colors

Font styles to use
Other font styles liked:
• Match Logo Font

Requirements
Must have
• Picture
• Logo
• Information on current business card
Should not have
• Lots of Colors

```html
<!DOCTYPE html>
<html lang="en">
<head>
<meta charset="utf-8">
<title>Northridge Realty – Business Card</title>
<link href="https://fonts.googleapis.com/css2?family=Open+Sans:wght@400;600;700&display=swap" rel="stylesheet">
<style>
  :root {
    --navy: #2c3d55;
    --sky: #3a9bd8;
    --paper: #ffffff;
    --ink: #2b3a4f;
    --stage: #e9e9e7;
  }
  * { box-sizing: border-box; margin: 0; padding: 0; }
  html, body { width: 1200px; height: 1000px; overflow: hidden; }
  body {
    background: var(--stage);
    font-family: "Open Sans", Arial, sans-serif;
    position: relative;
  }
  .card {
    position: absolute;
    left: 266px;
    width: 666px;
    height: 395px;
    overflow: hidden;
    box-shadow: 0 4px 14px rgba(0,0,0,.18);
  }
  .card--front { top: 75px; background: var(--paper); }
  .card--back  { top: 534px; background: var(--navy); }

  /* brand name block */
  .brand {
    position: absolute;
    display: flex;
    align-items: center;
    font-weight: 700;
    text-transform: uppercase;
    white-space: nowrap;
  }
  .brand__dot { border-radius: 50%; background: var(--sky); flex: none; }
  .card--front .brand {
    left: 33px; top: 118px;
    gap: 10px;
    font-size: 23px; letter-spacing: 1px;
    color: var(--ink);
  }
  .card--front .brand__dot { width: 20px; height: 20px; }
  .card--back .brand {
    left: 0; right: 0; justify-content: center; top: 195px;
    gap: 14px;
    font-size: 40px; letter-spacing: 2px;
    color: var(--paper);
  }
  .card--back .brand__dot { width: 32px; height: 32px; }

  /* agent details */
  .agent { position: absolute; left: 33px; top: 198px; color: var(--ink); }
  .agent__name { font-size: 22px; font-weight: 600; line-height: 1.2; }
  .agent__role { font-size: 17px; color: var(--sky); margin-top: 2px; }
  .contact { list-style: none; margin-top: 16px; font-size: 15.5px; line-height: 24px; }
  .contact li { display: flex; align-items: center; gap: 7px; }
  .contact svg { width: 15px; height: 12px; fill: var(--sky); }
  .contact .contact__address { margin-top: 5px; }

  .headshot {
    position: absolute;
    left: 400px; top: 12px;
    width: 266px; height: 383px;
    background: linear-gradient(180deg, #c9b3a2 0%, #b79c88 30%, #a7b8cc 52%, #2a2c33 70%, #1d1f25 100%);
    clip-path: polygon(0 0, 100% 0, 100% 372px, 70% 352px, 35% 339px, 0 332px);
  }
  .footer-band { position: absolute; left: 0; top: 0; width: 666px; height: 395px; }
  .footer-badge {
    position: absolute; left: 32px; top: 357px;
    width: 20px; height: 24px; background: var(--paper);
  }
  .footer-url {
    position: absolute; left: 69px; top: 358px;
    font-size: 15.5px; color: var(--paper); letter-spacing: .5px;
  }
  .back-url {
    position: absolute; left: 0; right: 0; top: 346px;
    text-align: center; color: var(--paper);
    font-size: 16px; letter-spacing: 3.5px;
  }
</style>
</head>
<body>

<section class="card card--front">
  <div class="headshot" role="img" aria-label="Headshot of the agent in a dark suit and patterned tie"></div>

  <svg class="footer-band" viewBox="0 0 666 395" aria-hidden="true">
    <path d="M0,349 C200,344 430,352 666,395 L0,395 Z" fill="var(--navy)"/>
    <path d="M320,341 C470,342 580,360 666,381 L666,391 C580,370 470,350 320,342 Z" fill="var(--sky)"/>
  </svg>

  <div class="brand"><span class="brand__dot"></span>Northridge Realty</div>

  <div class="agent">
    <p class="agent__name">Dalton Reeve</p>
    <p class="agent__role">Real Estate Licensee</p>
    <ul class="contact">
      <li>
        <svg viewBox="0 0 15 12" aria-hidden="true"><path d="M1 3.5C3 1 12 1 14 3.5L12.5 5 10.5 4V3H4.5V4L2.5 5Z M3.5 6H11.5L13 11H2Z"/></svg>
        (907) 555-0148
      </li>
      <li>
        <svg viewBox="0 0 15 12" aria-hidden="true"><path d="M1 1.5H14V10.5H1Z" fill="none" stroke="#3a9bd8" stroke-width="1.4"/><path d="M1 1.5L7.5 7 14 1.5" fill="none" stroke="#3a9bd8" stroke-width="1.4"/></svg>
        dalton@northridgeak.com
      </li>
      <li class="contact__address">2210 W Birch Loop #108 Palmer, AK 99645</li>
    </ul>
  </div>

  <div class="footer-badge"></div>
  <p class="footer-url">www.northridgeak.com</p>
</section>

<section class="card card--back">
  <div class="brand"><span class="brand__dot"></span>Northridge Realty</div>
  <p class="back-url">www.northridgeak.com</p>
</section>

</body>
</html>
```